Velduna.com webside

I want to build a Velduna.com retail website use on Shopify, reselling three main categories: Office Supplies, Packing Supplies, and Home Consumables. I also wish the webpage has the same functions as the Corvelt home page. The page is split into three different parts with the top being a sliding screen showcasing promotion products, below it being the three categories, and finally, a moving screen showing company missions.
Target Market(s)
U.S online
Industry/Entity Type
Office Supplies, packing Supplies and Home Consumables
Coding
Coded - Design and coding required
Number of Pages Required
5+ page
Look and feel

```html
<!DOCTYPE html>
<html lang="en">
<head>
<meta charset="utf-8">
<title>Velduna — Office, Packing &amp; Home Supplies</title>
<link rel="stylesheet" href="https://fonts.googleapis.com/css2?family=Open+Sans:wght@400;600;700&family=Poppins:wght@400;600;700;800&family=Nunito+Sans:wght@400;600&display=swap">
<style>
:root{
  --green:#00a78e;
  --dark:#2b2b2b;
  --footer:#262626;
  --orange:#f4a51c;
  --ink:#1f1f1f;
  --muted:#555;
  --page:#f4f4f4;
  --tile:#f3f6f5;
  --hero:#ececec;
  --hero-band:#dcdcdd;
}
*{margin:0;padding:0;box-sizing:border-box}
html,body{width:1200px;height:2841px;overflow:hidden}
body{font-family:"Open Sans",sans-serif;background:var(--page);color:var(--ink);position:relative}
.abs{position:absolute}
a{color:inherit;text-decoration:none}

/* top bar */
.topbar{left:0;top:0;width:1200px;height:51px;background:var(--dark);color:#fff}
.account{left:652px;top:8px;font-size:12px;line-height:15px}
.account b{font-size:15px;font-weight:600;display:block}
.returns{left:836px;top:7px;font-size:16px;line-height:18px;font-weight:600}
.cart-icon{left:968px;top:0;width:56px;height:51px;background:var(--green)}
.cart-label{left:1032px;top:14px;font-size:16px;font-weight:600}

/* nav */
.nav{left:0;top:51px;width:1200px;height:79px;background:#fff}
.logo{left:109px;top:18px;font-size:36px;font-weight:400;color:var(--ink);letter-spacing:.5px}
.menu{left:258px;top:31px;display:flex;gap:17px;font-size:16px;color:#333}
.search{left:806px;top:14px;width:283px;height:53px;border:1px solid #bbb;border-radius:4px;background:#fff}
.search .scope{position:absolute;left:0;top:0;width:55px;height:51px;background:#f0f0f0;border-right:1px solid #ccc;font-size:16px;color:#555;padding:15px 0 0 10px}

/* hero */
.hero{left:0;top:130px;width:1200px;height:567px;background:var(--hero);overflow:hidden}
.hero .band{position:absolute;left:0;top:441px;width:1200px;height:126px;background:var(--hero-band)}
.hero-kicker{left:108px;top:107px;font-size:40px;font-family:"Poppins",sans-serif;font-weight:400;color:#222}
.hero-title{left:108px;top:150px;font-size:72px;font-family:"Poppins",sans-serif;font-weight:800;font-style:italic;color:#111;letter-spacing:1px}
.hero-sub{left:108px;top:250px;font-size:40px;font-family:"Poppins",sans-serif;color:#222}
.btn-shop{left:111px;top:325px;width:190px;height:66px;border-radius:33px;background:var(--green);color:#fff;font-size:20px;font-weight:600;text-align:center;line-height:66px}
.badge{left:496px;top:41px;width:124px;height:124px;border-radius:50%;background:var(--orange);color:#fff;text-align:center;padding-top:20px;line-height:1}
.badge b{font-size:31px;font-weight:700;display:block}
.badge span{font-size:20px;display:block;margin-top:3px}
.badge small{font-size:14px;display:block;margin-top:3px}
.dots{left:111px;top:491px;display:flex;gap:5px}
.dots i{width:12px;height:12px;border-radius:50%;background:#bbb;display:block}
.dots i.on{background:#fff}

/* categories */
.section-title{left:0;top:758px;width:1200px;text-align:center;font-family:"Poppins",sans-serif;font-weight:700;font-size:38px;letter-spacing:.5px}
.card{background:#fff}
.card h3{position:absolute;left:31px;top:31px;font-family:"Nunito Sans",sans-serif;font-weight:400;font-size:30px;padding-left:16px;border-left:6px solid var(--green);line-height:42px}
.tile{position:absolute;background:var(--tile);text-align:center;font-size:17px;color:#444;line-height:22px}
.tile .pic{display:block;margin:10px auto 0;border-radius:6px}
.tile p{position:absolute;left:0;right:0;bottom:12px}
.view-all{position:absolute;font-size:18px;font-weight:600;color:var(--green)}

/* mission */
.mission-bg{left:0;top:1867px}
.mission-title{left:110px;top:1918px;font-family:"Poppins",sans-serif;font-weight:700;font-size:40px;color:#fff}
.mission-text{left:111px;top:1988px;width:410px;font-size:16.5px;line-height:25px;color:#fff}
.btn-read{left:111px;top:2141px;width:163px;height:58px;border-radius:29px;background:#fff;color:#222;font-size:18px;font-weight:600;text-align:center;line-height:58px}
.video{left:564px;top:1914px;width:523px;height:326px;background:linear-gradient(135deg,#b98a79 0%,#8a6456 40%,#4f6a78 75%,#2f3f4a 100%)}
.play{left:796px;top:2047px;width:60px;height:60px;border-radius:50%;background:rgba(20,20,20,.75)}

/* signup */
.signup{left:111px;top:2335px;border-left:6px solid var(--green);padding-left:15px;font-family:"Nunito Sans",sans-serif;font-size:29px;line-height:34px;color:#222;width:400px}
.email{left:536px;top:2354px;width:490px;height:62px;background:#fff;font-size:17px;color:#555;padding:20px 0 0 26px}
.send{left:1026px;top:2354px;width:63px;height:62px;background:var(--green)}

/* footer */
.footer{left:0;top:2475px;width:1200px;height:366px;background:var(--footer);color:#fff}
.fcol{position:absolute;top:64px}
.fcol h4{font-size:18px;font-weight:600;margin-bottom:18px}
.fcol li{list-style:none;font-size:16px;line-height:27.5px}
.contact{font-size:16px;line-height:27.5px}
.divider{position:absolute;left:111px;top:266px;width:978px;height:1px;background:#555}
.copy{position:absolute;left:111px;top:302px;font-size:16px}
.social{position:absolute;top:293px;width:38px;height:38px;border-radius:50%;border:1.5px solid var(--green)}
</style>
</head>
<body>

<header>
  <div class="abs topbar">
    <svg class="abs" style="left:651px;top:9px" width="12" height="14" viewBox="0 0 12 14"><circle cx="6" cy="4" r="3.5" fill="#fff"/><path d="M0 14c0-4 2.5-6 6-6s6 2 6 6z" fill="#fff"/></svg>
    <div class="abs account" style="left:670px">Hello, Sign in<b>Accounts &amp; Lists ▾</b></div>
    <svg class="abs" style="left:836px;top:9px" width="16" height="16" viewBox="0 0 16 16"><path d="M3 8a5 5 0 1 0 1.6-3.7" fill="none" stroke="#fff" stroke-width="2"/><path d="M2 1v5h5" fill="none" stroke="#fff" stroke-width="2"/></svg>
    <div class="abs returns" style="left:858px">Returns &amp;<br>Orders</div>
    <div class="abs cart-icon">
      <svg style="margin:12px 0 0 12px" width="34" height="28" viewBox="0 0 34 28"><path d="M1 2h6l4 16h18l4-12H9" fill="none" stroke="#fff" stroke-width="2.5" stroke-linejoin="round"/><circle cx="13" cy="24" r="2.5" fill="#fff"/><circle cx="27" cy="24" r="2.5" fill="#fff"/></svg>
    </div>
    <div class="abs cart-label">Cart (0)</div>
  </div>

  <nav class="abs nav">
    <div class="abs logo">Velduna</div>
    <div class="abs menu">
      <span>☰ All</span><span>Today's Deals</span><span>Customer Service</span><span>Registry</span><span>Gift Cards</span><span>Sell</span>
    </div>
    <div class="abs search">
      <div class="scope">All ⌄</div>
      <svg style="position:absolute;right:9px;top:15px" width="22" height="22" viewBox="0 0 22 22"><circle cx="9" cy="9" r="7" fill="none" stroke="#444" stroke-width="2.5"/><path d="M14 14l6 6" stroke="#444" stroke-width="3" stroke-linecap="round"/></svg>
    </div>
  </nav>
</header>

<section class="abs hero">
  <div class="band"></div>
  <svg class="abs" style="left:0;top:0" width="1200" height="567"><polygon points="1060,0 1200,0 1200,567 852,567" fill="var(--green)"/></svg>
  <div class="abs" role="img" aria-label="Packing supplies: open cardboard box with bubble wrap, tape dispenser, twine and mailing tube" style="left:474px;top:46px;width:640px;height:497px;background:radial-gradient(ellipse at 60% 55%,#c89b6a 0%,#b88a5c 45%,rgba(200,160,110,.35) 70%,rgba(236,236,236,0) 85%)"></div>
  <div class="abs hero-kicker">FOR ALL YOUR</div>
  <div class="abs hero-title">PACKING</div>
  <div class="abs hero-sub">NEEDS</div>
  <a class="abs btn-shop">SHOP NOW</a>
  <div class="abs badge"><b>30%</b><span>OFF</span><small>Limited Time</small></div>
  <div class="abs dots"><i></i><i class="on"></i><i></i></div>
</section>

<main>
  <h2 class="abs section-title">PRODUCT CATEGORIES</h2>

  <div class="abs card" style="left:111px;top:846px;width:470px;height:555px">
    <h3>Office Supplies</h3>
    <div class="tile" style="left:35px;top:97px;width:196px;height:190px"><span class="pic" role="img" aria-label="Desk organizer with pens" style="width:70px;height:120px;background:linear-gradient(#3a3a3a,#111)"></span><p>Multi Storage<br>Desk Organizer</p></div>
    <div class="tile" style="left:240px;top:97px;width:196px;height:190px"><span class="pic" role="img" aria-label="Blue desk mat" style="width:160px;height:70px;margin-top:35px;background:linear-gradient(#6fd0ff,#1a8fe0);border-radius:30px"></span><p>Leather<br>Desk Mat</p></div>
    <div class="tile" style="left:35px;top:296px;width:196px;height:190px"><span class="pic" role="img" aria-label="Red mouse pad" style="width:140px;height:80px;margin-top:30px;background:linear-gradient(#ff4a55,#d81c28)"></span><p>Lorem ipisum<br>Mouse pad</p></div>
    <div class="tile" style="left:240px;top:296px;width:196px;height:190px"><span class="pic" role="img" aria-label="2022 spiral notebook" style="width:95px;height:120px;background:linear-gradient(#9a9ab5,#6f6f8c)"></span><p>Personalized<br>Notebook</p></div>
    <a class="view-all" style="left:47px;top:508px">VIEW ALL</a>
  </div>

  <div class="abs card" style="left:614px;top:846px;width:470px;height:555px">
    <h3>Packing Supplies</h3>
    <div class="tile" style="left:35px;top:97px;width:196px;height:190px"><span class="pic" role="img" aria-label="Courier poly bag" style="width:70px;height:120px;background:linear-gradient(#3a3a3a,#111)"></span><p>Courier<br>Poly bag</p></div>
    <div class="tile" style="left:240px;top:97px;width:196px;height:190px"><span class="pic" role="img" aria-label="Open cardboard tuck box" style="width:130px;height:110px;background:linear-gradient(#e7b27a,#c98b4f)"></span><p>Reverse<br>Tuck Box</p></div>
    <div class="tile" style="left:35px;top:296px;width:196px;height:190px"><span class="pic" role="img" aria-label="Roll of bubble wrap" style="width:170px;height:100px;margin-top:20px;background:linear-gradient(#f4f6f7,#cfd4d8)"></span><p>Bubble<br>Wrap</p></div>
    <div class="tile" style="left:240px;top:296px;width:196px;height:190px"><span class="pic" role="img" aria-label="Black strapping tape roll" style="width:170px;height:95px;margin-top:15px;background:linear-gradient(#444,#0d0d0d)"></span><p>Strapping<br>tape</p></div>
    <a class="view-all" style="left:47px;top:508px">VIEW ALL</a>
  </div>

  <div class="abs card" style="left:111px;top:1432px;width:973px;height:366px">
    <h3>Home Consumables</h3>
    <div class="tile" style="left:8px;top:103px;width:185px;height:192px"><span class="pic" role="img" aria-label="Blue dust pan with brush" style="width:120px;height:110px;background:linear-gradient(#3aa0f0,#0c6fd1)"></span><p>Dust Pan<br>with brush</p></div>
    <div class="tile" style="left:202px;top:103px;width:185px;height:192px"><span class="pic" role="img" aria-label="Yellow rubber gloves" style="width:160px;height:110px;background:linear-gradient(#ffe24a,#e9b800)"></span><p>Rubber<br>Gloves</p></div>
    <div class="tile" style="left:396px;top:103px;width:185px;height:192px"><span class="pic" role="img" aria-label="Blue spray cleaner bottle" style="width:55px;height:120px;background:linear-gradient(#7fd6ff,#1089d8)"></span><p>Spray<br>Cleaner</p></div>
    <div class="tile" style="left:590px;top:103px;width:185px;height:192px"><span class="pic" role="img" aria-label="Sponge mop head" style="width:120px;height:110px;border-radius:50%;background:radial-gradient(#9ee33a 20%,#f2f2f2 45%,#dcdcdc 80%)"></span><p>Sponge<br>Mop</p></div>
    <div class="tile" style="left:784px;top:103px;width:185px;height:192px"><span class="pic" role="img" aria-label="Paper towel roll" style="width:150px;height:110px;background:linear-gradient(#ffffff,#dcdcdc)"></span><p>Paper<br>Towel</p></div>
    <a class="view-all" style="left:49px;top:318px">VIEW ALL</a>
  </div>

  <section>
    <svg class="abs mission-bg" width="680" height="420"><polygon points="0,0 607,0 673,420 0,420" fill="var(--green)"/></svg>
    <h2 class="abs mission-title">OUR MISSION</h2>
    <p class="abs mission-text">Lorem ipsum dolor sit amet, consectetur adipiscing elit, sed do eiusmod tempor incididunt ut labore et dolore magna aliqua. Ut enim ad minim veniam, quis nostrud exercitation ullamco laboris nisi ut aliquip ex ea commodo consequat.</p>
    <a class="abs btn-read">READ MORE</a>
    <div class="abs video" role="img" aria-label="Video still: hands shopping on a smartphone"></div>
    <div class="abs play"><svg width="60" height="60" viewBox="0 0 60 60"><polygon points="24,18 43,30 24,42" fill="#fff"/></svg></div>
  </section>

  <section>
    <p class="abs signup">Sign up now to get alerts for new product drops and rad promotions</p>
    <div class="abs email">Email Address</div>
    <div class="abs send"><svg width="63" height="62" viewBox="0 0 63 62"><path d="M20 32l24-12-7 24-5-8z" fill="#fff"/><path d="M32 36l12-16" stroke="var(--green)" stroke-width="2"/></svg></div>
  </section>
</main>

<footer class="abs footer">
  <div class="fcol" style="left:112px"><h4>Get To Know us</h4><ul><li>Our Story</li><li>Careers</li><li>Blog</li></ul></div>
  <div class="fcol" style="left:323px"><h4>Quick links</h4><ul><li>Today's Deals</li><li>Customer Service</li><li>Registry</li><li>Gift Cards</li><li>Sell</li></ul></div>
  <div class="fcol" style="left:528px"><h4>Let us help you</h4><ul><li>Your Account</li><li>Your Orders</li><li>Shipping Rates &amp; Policies</li><li>Returns &amp; Replacements</li></ul></div>
  <div class="fcol contact" style="left:790px">
    <h4>Need Help?</h4>
    <p>We're here to help you with your order!</p>
    <p style="margin-top:16px"><svg width="14" height="14" viewBox="0 0 14 14" style="vertical-align:-1px"><path d="M3 1l2.5 3-1.5 1.5c.8 1.8 2.2 3.2 4 4L9.5 8 13 10.5 11.5 13C6 13 1 8 1 2.5z" fill="var(--green)"/></svg> 1 800 555 0142</p>
    <p style="margin-top:8px"><svg width="14" height="11" viewBox="0 0 14 11" style="vertical-align:-1px"><rect width="14" height="11" fill="var(--green)"/><path d="M0 0l7 6 7-6" fill="none" stroke="#262626" stroke-width="1.3"/></svg> info@velduna.com</p>
  </div>
  <div class="divider"></div>
  <p class="copy">© 2022, Velduna. All rights reserved.</p>
  <span class="social" style="left:962px" aria-label="Social profile"></span>
  <span class="social" style="left:1006px" aria-label="Social profile"></span>
  <span class="social" style="left:1050px" aria-label="Social profile"></span>
</footer>

</body>
</html>
```